2019 2020 School Leavers Flyer

refer attached hoodie and tee shirts flyers for 2018, we just require an updated version showing 2019 and 2020 designs.we would like to do it as an A3 flyer folded to A4, so we will need a front and back cover.we would also like to use our new KVR logo (different versions attached) happy for any to be used creatively.back cover could be an advertisement that gets customers to visit our website.www.kelvaroutfitters.com.au
Target Market(s)
Schools buying leavers tee shirts and hoodies for their students
Requirements
Must have
- plenty of design options similar to flyers i have already attached
Nice to have
- back page , just an advertisement to get visitors to our website

```html
<!DOCTYPE html>
<html lang="en">
<head>
<meta charset="utf-8">
<title>KVR Leavers Hoodie and Tee Shirts Flyer 2019–2020</title>
<link rel="stylesheet" href="https://fonts.googleapis.com/css2?family=Alfa+Slab+One&family=Montserrat:wght@500;700;800&display=swap">
<style>
  :root {
    --stage: #8fbccd;
    --paper: #f4f4f4;
    --paper-shade: #e4e4e4;
    --red: #d71f1a;
    --red-dark: #b3140f;
    --orange: #f07a1a;
    --ink: #1c1c1c;
    --grey: #c9c9c9;
    --white: #ffffff;
    --tee-white: #fbfbfb;
  }
  * { box-sizing: border-box; margin: 0; padding: 0; }
  html, body { width: 1200px; height: 752px; overflow: hidden; }
  body {
    background: var(--stage);
    font-family: "Montserrat", sans-serif;
    position: relative;
  }
  .page {
    position: absolute;
    top: 93px;
    width: 400px;
    height: 566px;
    background: linear-gradient(180deg, var(--white) 0%, var(--paper) 60%, var(--paper-shade) 100%);
    overflow: hidden;
    box-shadow: 0 10px 24px rgba(0,0,0,0.22);
  }
  .page--front { left: 160px; }
  .page--back { left: 640px; }

  /* Front cover */
  .ribbon { position: absolute; left: 0; top: 0; width: 400px; height: 200px; }
  .ribbon-text {
    position: absolute; left: 60px; top: 40px; width: 270px;
    color: var(--white); text-align: center; text-transform: uppercase;
    font-weight: 800; line-height: 1.15;
  }
  .ribbon-text .line { font-size: 14px; letter-spacing: 0.5px; }
  .ribbon-text .years { font-size: 24px; }
  .ribbon-text .cta { font-size: 17px; }
  .ribbon-text .web { font-size: 9px; font-weight: 500; text-transform: none; margin-top: 3px; }

  .brand-badge {
    position: absolute; left: 292px; top: 108px;
    width: 88px; height: 88px; border-radius: 50%;
    background: var(--white); border: 4px solid var(--red);
    display: flex; align-items: center; justify-content: center;
  }
  .brand-name {
    font-family: "Montserrat", sans-serif; font-weight: 800;
    font-size: 24px; color: var(--ink); letter-spacing: 1px;
  }

  .garment-grid {
    position: absolute; display: grid;
    grid-template-columns: repeat(4, 72px); column-gap: 12px;
  }
  .garment-grid--hoodies { left: 38px; top: 214px; grid-auto-rows: 68px; }
  .garment-grid--tees { left: 38px; top: 180px; grid-auto-rows: 76px; }
  .garment { display: flex; flex-direction: column; align-items: center; }
  .garment-shape {
    width: 54px; height: 48px; border-radius: 16px 16px 6px 6px;
    background: var(--ink);
  }
  .garment-shape--white {
    background: var(--tee-white); border: 1px solid var(--grey);
    border-radius: 10px 10px 4px 4px;
  }
  .garment-shape--black-tee { border-radius: 10px 10px 4px 4px; }
  .garment-label {
    font-size: 6px; font-weight: 700; color: #555; margin-top: 4px;
    text-transform: uppercase; letter-spacing: 0.4px;
  }

  .footer-band { position: absolute; left: 0; bottom: 0; width: 400px; height: 80px; }
  .contact {
    position: absolute; color: var(--white); font-weight: 700;
    display: flex; align-items: center; gap: 6px;
  }
  .contact svg { width: 11px; height: 11px; fill: var(--white); }
  .page--front .contact { left: 140px; bottom: 14px; font-size: 14px; }

  /* Back cover */
  .crest { position: absolute; left: 0; top: 0; width: 400px; height: 104px; }
  .crest-brand { position: absolute; left: 0; top: 34px; width: 400px; text-align: center; }
  .collection-title {
    position: absolute; left: 0; top: 116px; width: 400px; text-align: center;
  }
  .collection-title h1 {
    font-family: "Alfa Slab One", serif; font-weight: 400;
    font-size: 20px; color: var(--red); letter-spacing: 1px; line-height: 1.2;
  }
  .collection-title p { font-size: 15px; font-weight: 800; color: var(--ink); }
  .page--back .contact { font-size: 10px; bottom: 22px; }
  .page--back .contact--phone { left: 24px; }
  .page--back .contact--web { right: 22px; }
</style>
</head>
<body>

<section class="page page--front" aria-label="Front cover">
  <svg class="ribbon" viewBox="0 0 400 200" aria-hidden="true">
    <polygon points="40,28 370,28 352,162 160,162 88,198 108,162 58,162" fill="var(--red)"/>
    <polygon points="370,28 392,24 378,70" fill="var(--red-dark)"/>
  </svg>
  <div class="ribbon-text">
    <div class="line">Our new design</div>
    <div class="line">Hoodie and tee shirts</div>
    <div class="years">2019 and 2020</div>
    <div class="cta">Visit our website</div>
    <div class="web">www.kelvaroutfitters.com.au</div>
  </div>
  <div class="brand-badge"><span class="brand-name">KVR</span></div>

  <div class="garment-grid garment-grid--hoodies">
    <div class="garment"><div class="garment-shape" role="img" aria-label="Black hoodie, design 1"></div><span class="garment-label">Design 1</span></div>
    <div class="garment"><div class="garment-shape" role="img" aria-label="Black hoodie, design 2"></div><span class="garment-label">Design 2</span></div>
    <div class="garment"><div class="garment-shape" role="img" aria-label="Black hoodie, design 3"></div><span class="garment-label">Design 3</span></div>
    <div class="garment"><div class="garment-shape" role="img" aria-label="Black hoodie, design 4"></div><span class="garment-label">Design 4</span></div>
    <div class="garment"><div class="garment-shape" role="img" aria-label="Black hoodie, design 5"></div><span class="garment-label">Design 5</span></div>
    <div class="garment"><div class="garment-shape" role="img" aria-label="Black hoodie, design 6"></div><span class="garment-label">Design 6</span></div>
    <div class="garment"><div class="garment-shape" role="img" aria-label="Black hoodie, design 7"></div><span class="garment-label">Design 7</span></div>
    <div class="garment"><div class="garment-shape" role="img" aria-label="Black hoodie, design 8"></div><span class="garment-label">Design 8</span></div>
    <div class="garment"><div class="garment-shape" role="img" aria-label="Black hoodie, design 9"></div><span class="garment-label">Design 9</span></div>
    <div class="garment"><div class="garment-shape" role="img" aria-label="Black hoodie, design 10"></div><span class="garment-label">Design 10</span></div>
    <div class="garment"><div class="garment-shape" role="img" aria-label="Black hoodie, design 11"></div><span class="garment-label">Design 11</span></div>
    <div class="garment"><div class="garment-shape" role="img" aria-label="Black hoodie, design 12"></div><span class="garment-label">Design 12</span></div>
    <div class="garment"><div class="garment-shape" role="img" aria-label="Black hoodie, design 13"></div><span class="garment-label">Design 13</span></div>
    <div class="garment"><div class="garment-shape" role="img" aria-label="Black hoodie, design 14"></div><span class="garment-label">Design 14</span></div>
    <div class="garment"><div class="garment-shape" role="img" aria-label="Black hoodie, design 15"></div><span class="garment-label">Design 15</span></div>
    <div class="garment"><div class="garment-shape" role="img" aria-label="Black hoodie, design 16"></div><span class="garment-label">Design 16</span></div>
  </div>

  <svg class="footer-band" viewBox="0 0 400 80" preserveAspectRatio="none" aria-hidden="true">
    <path d="M0,10 Q200,42 400,22 L400,80 L0,80 Z" fill="var(--red)"/>
    <path d="M0,0 Q200,34 400,12 L400,22 Q200,42 0,10 Z" fill="var(--red-dark)"/>
  </svg>
  <div class="contact">
    <svg viewBox="0 0 24 24" aria-hidden="true"><path d="M6.6 10.8a15.1 15.1 0 0 0 6.6 6.6l2.2-2.2a1 1 0 0 1 1-.25 11.4 11.4 0 0 0 3.6.57 1 1 0 0 1 1 1V20a1 1 0 0 1-1 1A17 17 0 0 1 3 4a1 1 0 0 1 1-1h3.5a1 1 0 0 1 1 1c0 1.25.2 2.45.57 3.570a1 1 0 0 1-.25 1z"/></svg>
    03 5550 1842
  </div>
</section>

<section class="page page--back" aria-label="Back cover">
  <svg class="crest" viewBox="0 0 400 104" aria-hidden="true">
    <defs>
      <radialGradient id="crestFill" cx="50%" cy="0%" r="80%">
        <stop offset="0%" stop-color="#ffffff"/>
        <stop offset="100%" stop-color="#bdbdbd"/>
      </radialGradient>
    </defs>
    <path d="M60,0 A140,100 0 0 0 340,0 Z" fill="url(#crestFill)"/>
    <path d="M72,0 A128,90 0 0 0 328,0" fill="none" stroke="var(--orange)" stroke-width="4"/>
    <path d="M60,0 A140,100 0 0 0 340,0" fill="none" stroke="var(--red)" stroke-width="3"/>
    <rect x="0" y="0" width="40" height="8" fill="var(--red)"/>
  </svg>
  <div class="crest-brand"><span class="brand-name">KVR</span></div>

  <div class="collection-title">
    <h1>HOODIE AND TEE SHIRTS</h1>
    <p>2019 AND 2020</p>
  </div>

  <div class="garment-grid garment-grid--tees">
    <div class="garment"><div class="garment-shape garment-shape--black-tee" role="img" aria-label="Black tee shirt, design 1"></div><span class="garment-label">Design 1</span></div>
    <div class="garment"><div class="garment-shape garment-shape--black-tee" role="img" aria-label="Black tee shirt, design 2"></div><span class="garment-label">Design 2</span></div>
    <div class="garment"><div class="garment-shape garment-shape--black-tee" role="img" aria-label="Black tee shirt, design 3"></div><span class="garment-label">Design 3</span></div>
    <div class="garment"><div class="garment-shape garment-shape--black-tee" role="img" aria-label="Black tee shirt, design 4"></div><span class="garment-label">Design 4</span></div>
    <div class="garment"><div class="garment-shape garment-shape--black-tee" role="img" aria-label="Black tee shirt, design 5"></div><span class="garment-label">Design 5</span></div>
    <div class="garment"><div class="garment-shape garment-shape--black-tee" role="img" aria-label="Black tee shirt, design 6"></div><span class="garment-label">Design 6</span></div>
    <div class="garment"><div class="garment-shape garment-shape--black-tee" role="img" aria-label="Black tee shirt, design 7"></div><span class="garment-label">Design 7</span></div>
    <div class="garment"><div class="garment-shape garment-shape--black-tee" role="img" aria-label="Black tee shirt, design 8"></div><span class="garment-label">Design 8</span></div>
    <div class="garment"><div class="garment-shape garment-shape--white" role="img" aria-label="White tee shirt, design 9"></div><span class="garment-label">Design 9</span></div>
    <div class="garment"><div class="garment-shape garment-shape--white" role="img" aria-label="White tee shirt, design 10"></div><span class="garment-label">Design 10</span></div>
    <div class="garment"><div class="garment-shape garment-shape--white" role="img" aria-label="White tee shirt, design 11"></div><span class="garment-label">Design 11</span></div>
    <div class="garment"><div class="garment-shape garment-shape--white" role="img" aria-label="White tee shirt, design 12"></div><span class="garment-label">Design 12</span></div>
    <div class="garment"><div class="garment-shape garment-shape--white" role="img" aria-label="White tee shirt, design 13"></div><span class="garment-label">Design 13</span></div>
    <div class="garment"><div class="garment-shape garment-shape--white" role="img" aria-label="White tee shirt, design 14"></div><span class="garment-label">Design 14</span></div>
    <div class="garment"><div class="garment-shape garment-shape--white" role="img" aria-label="White tee shirt, design 15"></div><span class="garment-label">Design 15</span></div>
    <div class="garment"><div class="garment-shape garment-shape--white" role="img" aria-label="White tee shirt, design 16"></div><span class="garment-label">Design 16</span></div>
  </div>

  <svg class="footer-band" viewBox="0 0 400 80" preserveAspectRatio="none" aria-hidden="true">
    <path d="M0,14 Q200,30 400,44 L400,80 L0,80 Z" fill="var(--red)"/>
    <path d="M0,4 Q200,20 400,34 L400,44 Q200,30 0,14 Z" fill="var(--red-dark)"/>
  </svg>
  <div class="contact contact--phone">
    <svg viewBox="0 0 24 24" aria-hidden="true"><path d="M6.6 10.8a15.1 15.1 0 0 0 6.6 6.6l2.2-2.2a1 1 0 0 1 1-.25 11.4 11.4 0 0 0 3.6.57 1 1 0 0 1 1 1V20a1 1 0 0 1-1 1A17 17 0 0 1 3 4a1 1 0 0 1 1-1h3.5a1 1 0 0 1 1 1c0 1.25.2 2.45.57 3.57a1 1 0 0 1-.25 1z"/></svg>
    03 5550 1842
  </div>
  <div class="contact contact--web">www.kelvaroutfitters.com.au</div>
</section>

</body>
</html>
```